Bref créative
Modern Business Name Card for IT Company
qLumio Sdn Bhd
Simple
Marissa Tanaka
Senior Manager
Lot C-17, 5B Floor,
8 Kilner Plaza,
No. 7, Jalan 24/6
47810 Petaling Jaya
Selangor, Malaysia
marissa@qlumiomarketing.example
www.qlumiomarketing.example
2187605-K
Kindly change the tagline of the website to a different font Segoe UI Semibold since the current font seem to rough and thick. Thanks.

```html
<!DOCTYPE html>
<html lang="en">
<head>
<meta charset="utf-8">
<title>qLumio Business Cards</title>
<link rel="stylesheet" href="https://fonts.googleapis.com/css2?family=Exo+2:wght@400;600;700&family=Open+Sans:wght@600&display=swap">
<style>
  :root {
    --bg: #e4e6ea;
    --navy: #1a2f86;
    --blue: #1f5fc4;
    --sky: #2f8fdc;
    --teal: #3fb4a8;
    --white: #ffffff;
    --ink: #1d4fb0;
    --soft: rgba(255,255,255,0.85);
  }
  * { box-sizing: border-box; margin: 0; padding: 0; }
  html, body { width: 1200px; height: 908px; overflow: hidden; }
  body {
    background: var(--bg);
    font-family: "Exo 2", sans-serif;
    position: relative;
  }
  .card {
    position: absolute;
    left: 250px;
    width: 700px;
    height: 400px;
    border-radius: 22px;
    overflow: hidden;
    box-shadow: 0 8px 24px rgba(0,0,0,0.18);
  }
  /* Brand side */
  .card-brand {
    top: 40px;
    background: linear-gradient(120deg, var(--navy) 0%, var(--blue) 55%, var(--sky) 100%);
  }
  .brand-circle {
    position: absolute;
    left: -70px; bottom: -90px;
    width: 380px; height: 380px;
    border-radius: 50%;
    background: rgba(63,180,168,0.22);
  }
  .brand-lockup {
    position: absolute;
    right: 60px; top: 140px;
    text-align: right;
    color: var(--white);
  }
  .brand-name {
    font-weight: 700;
    font-size: 86px;
    line-height: 1;
    letter-spacing: 2px;
  }
  .brand-tagline {
    font-family: "Open Sans", sans-serif;
    font-weight: 600;
    font-size: 16px;
    letter-spacing: 3px;
    margin-top: 10px;
    color: var(--soft);
  }
  /* Contact side */
  .card-contact {
    top: 468px;
    background: var(--white);
  }
  .contact-logo {
    position: absolute;
    left: 48px; top: 84px;
    display: flex; align-items: center; gap: 12px;
  }
  .logo-dot {
    width: 50px; height: 50px; border-radius: 50%;
    background: var(--sky);
  }
  .logo-name {
    font-weight: 700;
    font-size: 62px;
    line-height: 1;
    color: var(--ink);
    letter-spacing: 2px;
  }
  .name-band {
    position: absolute;
    left: 0; bottom: 0;
    width: 100%; height: 128px;
    background: linear-gradient(90deg, var(--sky) 0%, var(--blue) 60%, var(--navy) 100%);
  }
  .person {
    position: absolute;
    left: 56px; bottom: 36px;
    color: var(--white);
  }
  .person-name { font-weight: 600; font-size: 28px; }
  .person-title { font-weight: 400; font-size: 16px; margin-top: 2px; color: var(--soft); }
  .detail-panel {
    position: absolute;
    right: 0; top: 0;
    width: 300px; height: 272px;
    background: linear-gradient(180deg, var(--navy), var(--blue));
    clip-path: polygon(18% 0, 100% 0, 100% 100%, 0 100%);
    color: var(--white);
    padding: 26px 14px 0 72px;
    font-size: 11px;
    line-height: 1.45;
    white-space: nowrap;
  }
  .licence { font-weight: 600; margin-bottom: 8px; }
  .address { margin-bottom: 10px; }
  .contact-line { display: flex; align-items: center; gap: 7px; margin-bottom: 4px; }
  .contact-line svg { flex: none; }
</style>
</head>
<body>
  <section class="card card-brand">
    <div class="brand-circle"></div>
    <div class="brand-lockup">
      <div class="brand-name">qLumio</div>
      <div class="brand-tagline">www.qlumiomarketing.example</div>
    </div>
  </section>

  <section class="card card-contact">
    <div class="contact-logo">
      <div class="logo-dot"></div>
      <div class="logo-name">qLumio</div>
    </div>

    <div class="detail-panel">
      <div class="licence">Licence No. 2187605-K</div>
      <div class="address">
        Lot C-17, 5B Floor,<br>
        8 Kilner Plaza,<br>
        No. 7, Jalan 24/6<br>
        47810 Petaling Jaya<br>
        Selangor, Malaysia
      </div>
      <div class="contact-line">
        <svg width="12" height="12" viewBox="0 0 12 12"><rect x="1" y="2.5" width="10" height="7" rx="1" fill="none" stroke="#fff" stroke-width="1"/><path d="M1.5 3 6 6.5 10.5 3" fill="none" stroke="#fff" stroke-width="1"/></svg>
        marissa@qlumiomarketing.example
      </div>
      <div class="contact-line">
        <svg width="12" height="12" viewBox="0 0 12 12"><path d="M3 1.5 5 3.5 4 5c.8 1.5 1.6 2.3 3 3l1.5-1 2 2-1.2 1.5C6 10.5 1.5 6 1.5 2.7z" fill="#fff"/></svg>
        +603 5550 1942
      </div>
      <div class="contact-line">
        <svg width="12" height="12" viewBox="0 0 12 12"><circle cx="6" cy="6" r="4.8" fill="none" stroke="#fff" stroke-width="1"/><path d="M1.2 6h9.6M6 1.2c-2.4 3-2.4 6.6 0 9.6M6 1.2c2.4 3 2.4 6.6 0 9.6" fill="none" stroke="#fff" stroke-width="0.8"/></svg>
        www.qlumiomarketing.example
      </div>
    </div>

    <div class="name-band"></div>
    <div class="person">
      <div class="person-name">Marissa Tanaka</div>
      <div class="person-title">Senior Manager</div>
    </div>
  </section>
</body>
</html>
```